Guarenteed 3 page coded Wordpress Website Job*

Initial Job/budged is for 3 pages cobed wesbite only :

-Home
-Videos Production
- Animation Videos

I will require a couple of extra pages and will pay and negotiate this with the winner*

We are a video production company based in Sydney Australia specialises in tradition on site video production with camera crew, web animation videos and social media advertising. The website needs to portray a modern, sharp, young, trendy, advanced technology company and be mobile compatible. Mainly white background with colour added in banners and certain sections to lift the site. I have attached a full brief.

Target Market(s)

Small to medium businesses

Coding

Coded - Design and coding required

Number of Pages Required

3 page

Requirements
Must have
• Wordpress
• Fast loading
• Add Videos
• Add pages
• Add categories
• Sharp and professional design
• Please be creative and see breif for guide
Should not have
• NOT Cartoon looking.

```html
<!DOCTYPE html>
<html lang="en">
<head>
<meta charset="utf-8">
<title>ReelSpark Media</title>
<link href="https://fonts.googleapis.com/css2?family=Open+Sans:wght@400;600&family=Raleway:wght@400;500;600&display=swap" rel="stylesheet">
<style>
  :root{
    --canvas:#f4f4f4;
    --page:#ffffff;
    --orange:#ff6a00;
    --orange-light:#ff8a1e;
    --blue:#0a5cb5;
    --blue-dark:#064a94;
    --ink:#3a3a3a;
    --muted:#6d6d6d;
    --line:#dcdcdc;
    --field:#f6f6f6;
    --hero-dark:#2b2b2b;
    --hero-mid:#6a6a62;
  }
  *{box-sizing:border-box;margin:0;padding:0}
  html,body{width:1200px;height:1120px;overflow:hidden;background:var(--canvas);font-family:"Open Sans",sans-serif;color:var(--ink)}
  .page{position:absolute;left:184px;top:0;width:831px;height:1120px;background:var(--page);border-left:1px solid #e6e6e6;border-right:1px solid #e6e6e6}
  .abs{position:absolute}

  /* header */
  .brand{left:25px;top:56px;display:flex;align-items:center;gap:8px}
  .brand-mark{width:14px;height:14px;background:var(--orange);border-radius:50%}
  .brand-name{font-family:"Raleway",sans-serif;font-weight:600;font-size:23px;color:var(--blue);line-height:1}
  .search{left:599px;top:58px;width:212px;height:27px;border:1px solid #cfcfcf;background:#fbfbfb;display:flex;align-items:center;justify-content:space-between;padding:0 10px}
  .search span{font-size:10px;font-style:italic;color:#777}

  /* nav */
  .nav{left:0;top:98px;width:831px;height:44px;background:linear-gradient(#ff8420,var(--orange));display:flex}
  .nav a{font-family:"Raleway",sans-serif;font-weight:500;font-size:14px;color:#fff;text-decoration:none;display:flex;align-items:center;justify-content:center;border-right:1px solid rgba(255,255,255,.35)}
  .nav a:last-child{border-right:none}

  /* hero */
  .hero{left:0;top:142px;width:831px;height:345px;background:radial-gradient(circle at 62% 35%,#d9d8b0 0,#8d8c7c 14%,var(--hero-mid) 28%,#4a4a48 55%,var(--hero-dark) 100%)}
  .step{width:160px;text-align:center}
  .step svg{display:block;margin:0 auto}
  .step-label{font-family:"Raleway",sans-serif;font-weight:500;font-size:16px;color:#fff;margin-top:6px;white-space:nowrap}
  .dots{left:387px;top:313px;display:flex;gap:6px}
  .dots i{width:13px;height:13px;border-radius:50%;background:#fff;display:block}

  /* content */
  .card{width:256px}
  .card-media{height:122px}
  .card h2{font-family:"Raleway",sans-serif;font-weight:500;font-size:18px;color:var(--ink);margin-top:17px}
  .card p{font-size:10.5px;line-height:19px;color:var(--muted);margin-top:6px}
  .btn-blue{display:inline-block;margin-top:12px;width:115px;height:33px;line-height:33px;text-align:center;background:linear-gradient(var(--blue),var(--blue-dark));color:#fff;font-family:"Raleway",sans-serif;font-weight:600;font-size:14px}

  .contact{left:562px;top:503px;width:257px;height:319px;border:1px solid var(--line)}
  .contact-head{height:44px;background:linear-gradient(#0d66c4,var(--blue-dark));color:#fff;font-family:"Raleway",sans-serif;font-weight:500;font-size:17px;padding:12px 0 0 20px}
  .field{position:absolute;left:20px;width:220px;height:29px;border:1px solid #d5d5d5;background:linear-gradient(#fff,var(--field));font-size:10px;color:#666;padding:8px 12px}
  .consult{position:absolute;left:23px;top:166px;font-size:10.5px;color:var(--ink)}
  .radios{position:absolute;left:23px;top:188px;display:flex;gap:24px;font-size:10px;color:#666}
  .radios label{display:flex;align-items:center;gap:5px}
  .radios i{width:11px;height:11px;border:1px solid #bbb;border-radius:50%;display:block;background:#f8f8f8;position:relative}
  .radios i.on::after{content:"";position:absolute;left:2px;top:2px;width:5px;height:5px;border-radius:50%;background:#aaa}
  .btn-orange{position:absolute;left:22px;top:270px;width:218px;height:36px;background:linear-gradient(var(--orange-light),var(--orange));color:#fff;font-family:"Raleway",sans-serif;font-weight:600;font-size:15px;text-align:center;line-height:36px}

  /* footer */
  .footer{left:0;top:860px;width:831px;height:205px;border-top:1px solid var(--line);background:linear-gradient(#fff,#f2f2f2)}
  .col{top:34px}
  .col h3{font-family:"Raleway",sans-serif;font-weight:400;font-size:17px;color:var(--ink);margin-bottom:8px}
  .col li{list-style:none;font-size:11px;line-height:19px;color:var(--muted)}
  .social{display:flex;gap:8px;margin-top:6px}
  .social span{font-size:11px;font-weight:600;color:var(--blue)}
  .badge{left:584px;top:121px;width:62px;height:62px;border-radius:50%;background:radial-gradient(#2f4f8a,#1a2f5a);border:3px solid #c9c9c9}
  .bottom{left:0;top:1065px;width:831px;height:55px;border-top:1px solid #e3e3e3;background:linear-gradient(#fff,#f0f0f0);font-size:10px;color:#666;padding:19px 0 0 34px}
</style>
</head>
<body>
<div class="page">
  <header>
    <div class="abs brand"><span class="brand-mark"></span><span class="brand-name">ReelSpark Media</span></div>
    <div class="abs search"><span>Search here</span>
      <svg width="14" height="14" viewBox="0 0 14 14"><circle cx="6" cy="6" r="4.5" fill="none" stroke="#999" stroke-width="1.6"/><line x1="9.3" y1="9.3" x2="13" y2="13" stroke="#999" stroke-width="1.8"/></svg>
    </div>
  </header>

  <nav class="abs nav">
    <a href="#" style="width:114px">HOME</a>
    <a href="#" style="width:117px">ABOUT US</a>
    <a href="#" style="width:92px">VIDEO</a>
    <a href="#" style="width:127px">ANIMATION</a>
    <a href="#" style="width:118px">SERVICES</a>
    <a href="#" style="width:138px">CONTACT US</a>
  </nav>

  <section class="abs hero" role="img" aria-label="Rows of dark light bulbs with one glowing bulb">
    <div class="abs step" style="left:97px;top:80px">
      <svg width="124" height="134" viewBox="0 0 124 134"><polygon points="62,2 121,35 121,99 62,132 3,99 3,35" fill="var(--orange)" stroke="#fff" stroke-width="3"/><text x="62" y="84" text-anchor="middle" font-family="Raleway,sans-serif" font-size="48" fill="#fff">1</text></svg>
      <div class="step-label" style="margin-top:8px">STAND OUT WITH VIDEO</div>
    </div>
    <div class="abs step" style="left:336px;top:80px">
      <svg width="124" height="134" viewBox="0 0 124 134"><polygon points="62,2 121,35 121,99 62,132 3,99 3,35" fill="var(--orange)" stroke="#fff" stroke-width="3"/><text x="62" y="84" text-anchor="middle" font-family="Raleway,sans-serif" font-size="48" fill="#fff">2</text></svg>
      <div class="step-label" style="margin-top:3px">GO VIRAL WITH VIDEO</div>
    </div>
    <div class="abs step" style="left:577px;top:80px">
      <svg width="124" height="134" viewBox="0 0 124 134"><polygon points="62,2 121,35 121,99 62,132 3,99 3,35" fill="var(--blue)" stroke="#fff" stroke-width="3"/><text x="62" y="84" text-anchor="middle" font-family="Raleway,sans-serif" font-size="48" fill="#fff">3</text></svg>
      <div class="step-label" style="margin-top:3px">GET IN TOUCH</div>
    </div>
    <div class="abs dots"><i></i><i></i><i></i><i></i></div>
  </section>

  <main>
    <article class="abs card" style="left:18px;top:503px">
      <div class="card-media" role="img" aria-label="Silhouette of a camera operator filming on set" style="background:linear-gradient(90deg,#e8e8e8,#9a9a9a 45%,#f2f2f2)"></div>
      <h2>STAND OUT WITH VIDEO</h2>
      <p>In massa libero interdum nec interdum vel blandit sed nulla In ullamcorper est eget tempor cursus neque mi consectetuer mi a ultricies massa est sed nisl Class aptent taciti sociosqu ad litora torquent per conubia nostra per inceptos hymenaeos</p>
      <a class="btn-blue">READ MORE</a>
    </article>
    <article class="abs card" style="left:291px;top:503px">
      <div class="card-media" role="img" aria-label="Close-up of social media app icons on a screen" style="background:linear-gradient(135deg,#1d3f7a,#2a8fd0 50%,#c0303a)"></div>
      <h2>GO VIRAL WITH VIDEO</h2>
      <p>In massa libero interdum nec interdum vel blandit sed nulla In ullamcorper est eget tempor cursus neque mi consectetuer mi a ultricies massa est sed nisl Class aptent taciti sociosqu ad litora torquent per conubia nostra per inceptos hymenaeos</p>
      <a class="btn-blue" style="margin-left:1px">READ MORE</a>
    </article>

    <aside class="abs contact">
      <div class="contact-head">GET IN TOUCH</div>
      <div class="field" style="top:57px">Name</div>
      <div class="field" style="top:93px">Phone no.</div>
      <div class="field" style="top:128px">Email address</div>
      <div class="consult">I'd like a FREE CONSULTATION</div>
      <div class="radios"><label><i class="on"></i>YES</label><label><i></i>NO</label></div>
      <div class="field" style="top:208px;height:56px">I am keen to talk about...</div>
      <div class="btn-orange">SEND TO CONSULTANT</div>
    </aside>
  </main>

  <footer class="abs footer">
    <div class="abs col" style="left:46px"><h3>Company</h3><ul><li>In massa libero interdum</li><li>Nec interdum</li><li>Vel blandit sed</li><li>Nulla ullamcorper</li><li>Est eget tempor</li></ul></div>
    <div class="abs col" style="left:221px"><h3>Our Services</h3><ul><li>Class aptent taciti</li><li>Sociosqu ad</li><li>Litora torquent</li><li>Per conubia nostra</li><li>Etiam eleifen</li></ul></div>
    <div class="abs col" style="left:400px"><h3>Resources</h3><ul><li>In massa libero interdum</li><li>Nec interdum</li><li>Vel blandit sed</li><li>Nulla ullamcorper</li><li>Est eget tempor</li></ul></div>
    <div class="abs col" style="left:576px"><h3>Get in touch</h3><ul><li>Please connect with us anywhere</li></ul>
      <div class="social"><span>Chirper</span><span>Friendly</span><span>WorkNet</span><span>Circles</span></div>
    </div>
    <div class="abs badge"></div>
  </footer>

  <div class="abs bottom">© 2015 Company Name&nbsp; All right reserved&nbsp; Term of Use</div>
</div>
</body>
</html>
```